Zielgruppe
Ich biete Marketing und Beratung an. Meine Zielgruppe sind KMU's aber auch Einzelfirmen welche selbst keine Marketingabteilung haben.
Aufgabenstellung
Sie sollen mein bestehendes CI/CD von meiner Website www.velorusk.ch möglichst mit Farben, Formen und Schriften übernehmen. Es soll eine einfache Seite mit 3 Rubriken werden. Über mich / Mein Angebot (Philosophie, Schwerpunkte/Preise) / Kontakt. Impressum, AGB und Datenschutz sollen CH Konform integriert sein. Ich habe meine Domain bei serwanox.ch registriert. Diese soll dann für die neue Website eingerichtet werden und von der Pixolo Seite entfernt werden. Der Link für Kontrabu soll funktionieren. Bilder können von der Pixolo Seite entnommen werden. Da ich für meine Kunden viele Websiten erstellen lassen werde, suche ich einen Designer*in mit welcher ich auch nach dieser Website zusammen arbeiten könnte. Die Seite möchte ich danach selber pflegen können. Es wäre toll wenn sie mit Wordpress erstellt wird (muss aber nicht sein).

```html
<!DOCTYPE html>
<html lang="de">
<head>
<meta charset="utf-8">
<title>velorusk – Marketing &amp; Beratung</title>
<link href="https://fonts.googleapis.com/css2?family=Montserrat:ital,wght@0,500;0,600;0,700;0,800;1,800&family=Open+Sans:ital,wght@0,400;0,600;1,600&display=swap" rel="stylesheet">
<style>
:root{
  --green:#2fa67d;
  --green-soft:#e6f4ee;
  --ink:#1d1d1f;
  --text:#5c5f62;
  --muted:#8a8d90;
  --line:#e4e6e8;
  --grey-bg:#f3f3f3;
  --canvas:#eef3f0;
  --footer:#262626;
  --white:#ffffff;
}
*{box-sizing:border-box;margin:0;padding:0}
html,body{width:1200px;height:3107px;overflow:hidden}
body{background:var(--canvas);font-family:"Open Sans",Arial,sans-serif;color:var(--text)}
.page{position:absolute;left:50px;top:60px;width:1100px;background:var(--white);box-shadow:0 20px 60px rgba(0,0,0,.12)}
.eyebrow{font-family:"Montserrat",Arial,sans-serif;font-size:9px;letter-spacing:2px;color:var(--green);font-weight:600;text-transform:uppercase}
.section-title{font-family:"Montserrat",Arial,sans-serif;font-weight:700;color:var(--ink);font-size:25px;margin-top:8px}
.lead{font-size:11px;line-height:1.6;color:var(--text);margin-top:10px}
.center{text-align:center}

/* nav */
.nav{height:55px;background:#f1f5f3;display:flex;align-items:center;padding:0 100px;justify-content:space-between}
.brand{font-family:"Montserrat",Arial,sans-serif;font-weight:700;font-size:22px;color:var(--ink);display:flex;align-items:center;gap:7px}
.brand-square{width:9px;height:9px;background:var(--ink)}
.nav-links{display:flex;align-items:center;gap:22px;font-size:10px;color:#444}
.btn{display:inline-block;font-family:"Montserrat",Arial,sans-serif;font-weight:600;font-size:10px;border-radius:3px;padding:9px 14px}
.btn-green{background:var(--green);color:var(--white)}
.btn-white{background:var(--white);color:var(--green)}
.btn-outline{border:1.5px solid var(--white);color:var(--white)}

/* hero */
.hero{position:relative;height:580px;overflow:hidden}
.hero-photo{position:absolute;inset:0;background:radial-gradient(ellipse at 68% 45%,#6cc29e 0%,#4fb38a 35%,#3fa57b 80%)}
.hero-content{position:absolute;left:100px;top:140px;color:var(--white)}
.hero-content .eyebrow{color:#e6f6ef}
.hero-title{font-family:"Montserrat",Arial,sans-serif;font-style:italic;font-weight:800;font-size:46px;line-height:1.04;margin-top:18px;letter-spacing:.5px}
.hero-sub{font-size:13px;line-height:1.55;margin-top:18px;width:360px}
.hero-actions{margin-top:20px;display:flex;gap:12px}
.hero-actions .btn{padding:11px 20px}

/* about */
.about{min-height:540px;display:flex;align-items:center;padding:30px 100px;gap:40px}
.portrait{width:430px;height:480px;background:linear-gradient(135deg,#d6d6d6,#9c9c9c 55%,#6f6f6f);box-shadow:0 8px 20px rgba(0,0,0,.15);flex:none}
.about-text{width:420px}
.about-text h2{font-family:"Montserrat",Arial,sans-serif;font-weight:700;font-size:22px;color:var(--ink);margin:8px 0 18px}
.about-text p{font-size:10.5px;line-height:1.65;margin-bottom:12px}
.quote{border-left:3px solid var(--green);padding-left:12px;font-style:italic;font-weight:600;font-size:10.5px;color:var(--ink);line-height:1.6;margin:14px 0 24px}
.about-text h3{font-family:"Montserrat",Arial,sans-serif;font-size:12px;color:var(--ink);margin-bottom:10px}
.name-key{font-size:9.5px;line-height:1.75}
.name-key b{color:var(--ink)}

/* offer */
.offer{background:var(--grey-bg);padding:55px 100px 55px}
.cards{display:grid;grid-template-columns:repeat(3,1fr);gap:15px;margin-top:40px}
.card{background:var(--white);border-radius:4px;height:105px;padding:16px}
.icon-box{width:24px;height:24px;border-radius:4px;background:var(--green-soft);display:flex;align-items:center;justify-content:center}
.card h4{font-family:"Montserrat",Arial,sans-serif;font-size:11px;font-weight:600;color:var(--ink);margin-top:14px}
.card p{font-size:9px;color:var(--muted);margin-top:6px}
.philosophy{background:var(--white);border-radius:4px;margin-top:40px;padding:24px 25px}
.philosophy h4{font-family:"Montserrat",Arial,sans-serif;font-size:13px;color:var(--green);font-weight:600}
.philosophy p{font-size:10px;line-height:1.7;margin-top:12px;width:500px}

/* prices */
.prices{padding:60px 100px 60px}
.plans{display:flex;justify-content:center;gap:20px;margin-top:42px}
.plan{position:relative;width:270px;height:195px;border:1px solid var(--line);border-radius:4px;padding:22px 20px}
.plan.featured{border:1.5px solid var(--green)}
.badge{position:absolute;top:-8px;left:18px;background:var(--green);color:var(--white);font-size:7px;font-weight:600;border-radius:8px;padding:2px 8px}
.plan h4{font-family:"Montserrat",Arial,sans-serif;font-size:15px;color:var(--ink);font-weight:600}
.price{font-family:"Montserrat",Arial,sans-serif;font-weight:700;font-size:19px;color:var(--green);margin-top:6px}
.price small{font-size:9px;color:var(--muted);font-weight:500}
.plan ul{list-style:none;margin-top:14px}
.plan li{font-size:8.5px;color:var(--text);display:flex;align-items:center;gap:6px;height:20px}
.prices .cta{text-align:center;margin-top:28px}
.prices .cta .btn{padding:10px 22px}

/* contact */
.contact{background:var(--grey-bg);padding:50px 100px 60px}
.contact-grid{display:flex;justify-content:space-between;margin:40px 80px 0}
.contact-info h4{font-family:"Montserrat",Arial,sans-serif;font-size:12px;color:var(--ink);font-weight:600;margin-bottom:14px}
.info-row{display:flex;gap:10px;font-size:9px;line-height:1.5;margin-bottom:10px;align-items:flex-start}
.form{width:330px}
.form label{display:block;font-size:9px;color:var(--ink);margin-bottom:6px}
.field{background:var(--white);border:1px solid var(--line);border-radius:3px;height:28px;font-size:8.5px;color:#aaa;padding:8px;margin-bottom:16px}
.field.area{height:84px}
.submit{background:var(--green);color:var(--white);text-align:center;font-family:"Montserrat",Arial,sans-serif;font-weight:600;font-size:10px;padding:10px;border-radius:3px}

/* footer */
.footer{height:150px;background:var(--footer);color:#bdbdbd;position:relative}
.footer-cols{display:flex;padding:28px 100px 0}
.footer .brand{color:var(--white);width:310px}
.footer .brand-square{background:var(--white)}
.footer-col{width:310px;font-size:8.5px;line-height:1.75}
.footer-col h5{font-family:"Montserrat",Arial,sans-serif;color:var(--white);font-size:9px;margin-bottom:6px}
.footer-bottom{position:absolute;left:0;right:0;bottom:0;border-top:1px solid #3a3a3a;text-align:center;font-size:7.5px;color:#8a8a8a;padding:12px 0}
</style>
</head>
<body>
<main class="page">

  <header class="nav">
    <div class="brand"><span class="brand-square"></span>velorusk</div>
    <nav class="nav-links">
      <span>Über mich</span><span>Angebot</span><span>Preise</span><span>Kontakt</span>
      <span class="btn btn-green">Kostenlose Offerte</span>
    </nav>
  </header>

  <section class="hero">
    <div class="hero-photo" role="img" aria-label="Foto einer Frau am Laptop in einem hellen Büro, grün eingefärbt"></div>
    <div class="hero-content">
      <div class="eyebrow">Marketing &amp; Beratung</div>
      <h1 class="hero-title">KLAR.<br>INSPIRIEREND.<br>WIRKSAM.</h1>
      <p class="hero-sub">Dein Marketing Profi – Ihre externe Marketingabteilung für KMU und Einzelfirmen.</p>
      <div class="hero-actions">
        <span class="btn btn-white">Kostenlose Offerte verlangen</span>
        <span class="btn btn-outline">Mein Angebot</span>
      </div>
    </div>
  </section>

  <section class="about">
    <div class="portrait" role="img" aria-label="Schwarz-weiss Porträt der Inhaberin, an eine Wand gelehnt"></div>
    <div class="about-text">
      <div class="eyebrow">Über mich</div>
      <h2>Mirela Kovan</h2>
      <p>Mit langjähriger Erfahrung im Marketing unterstütze ich kleine und mittlere Unternehmen sowie Einzelfirmen als ihre externe Marketingabteilung – kompetent, persönlich und praxisnah.</p>
      <p>Mein Ansatz: Ich höre zu, verstehe Ihr Geschäft und entwickle massgeschneiderte Strategien, die wirklich funktionieren. Kein Marketing von der Stange, sondern individuelle Lösungen.</p>
      <div class="quote">«Durch meine Marketing Expertise hole ich das Beste aus Ihrem Unternehmen heraus.»</div>
      <h3>Was steht hinter velorusk?</h3>
      <div class="name-key"><b>Vel:</b> Branding<br><b>Oru:</b> Business<br><b>sk:</b> erzeugen, erneuen, kreieren</div>
    </div>
  </section>

  <section class="offer">
    <div class="center">
      <div class="eyebrow">Mein Angebot</div>
      <h2 class="section-title">Ihre externe Marketingabteilung</h2>
      <p class="lead">Professionelles Marketing muss nicht teuer sein. Ich biete Ihnen flexible Unterstützung –<br>genau dort, wo Sie sie brauchen.</p>
    </div>
    <div class="cards">
      <div class="card"><div class="icon-box"><svg width="12" height="12" viewBox="0 0 12 12" fill="none" stroke="#2fa67d" stroke-width="1.2"><circle cx="6" cy="6" r="5"/><circle cx="6" cy="6" r="2.5"/><circle cx="6" cy="6" r=".6" fill="#2fa67d"/></svg></div><h4>Marketing Strategie</h4><p>Individuelle Strategien für Ihr Wachstum.</p></div>
      <div class="card"><div class="icon-box"><svg width="12" height="12" viewBox="0 0 12 12" fill="none" stroke="#2fa67d" stroke-width="1.2"><path d="M6 1a5 5 0 1 0 0 10c1 0 1-1 .5-1.7S6.5 7.5 8 7.5h1.5A1.5 1.5 0 0 0 11 6 5 5 0 0 0 6 1z"/></svg></div><h4>Branding</h4><p>Markenidentität, die überzeugt und bleibt.</p></div>
      <div class="card"><div class="icon-box"><svg width="12" height="12" viewBox="0 0 12 12" fill="none" stroke="#2fa67d" stroke-width="1.2"><path d="M1 9l3.5-3.5 2 2L11 3M8 3h3v3"/></svg></div><h4>Product Management</h4><p>Von der Idee bis zum erfolgreichen Launch.</p></div>
      <div class="card"><div class="icon-box"><svg width="12" height="12" viewBox="0 0 12 12" fill="none" stroke="#2fa67d" stroke-width="1.2"><path d="M1.5 5v2h2l5 3V2l-5 3z"/></svg></div><h4>Werbe- und Kommunikationsplanung</h4><p>Zielgerichtete Kampagnen mit Wirkung.</p></div>
      <div class="card"><div class="icon-box"><svg width="12" height="12" viewBox="0 0 12 12" fill="none" stroke="#2fa67d" stroke-width="1.2"><circle cx="4.5" cy="4" r="2"/><path d="M1 10.5a3.5 3.5 0 0 1 7 0"/><circle cx="8.5" cy="4.5" r="1.5"/><path d="M9 7.5a2.5 2.5 0 0 1 2 2.5"/></svg></div><h4>Beratung</h4><p>Sparringspartner auf Augenhöhe.</p></div>
      <div class="card"><div class="icon-box"><svg width="12" height="12" viewBox="0 0 12 12" fill="none" stroke="#2fa67d" stroke-width="1.2"><path d="M1 4.5L6 2l5 2.5L6 7z"/><path d="M3 5.5V8c1.8 1.3 4.2 1.3 6 0V5.5"/></svg></div><h4>Events, Workshops, Schulungen</h4><p>Wissen vermitteln, Teams stärken.</p></div>
    </div>
    <div class="philosophy">
      <h4>Meine Philosophie</h4>
      <p>Jedes Unternehmen ist einzigartig – und verdient ein Marketing, das genau das widerspiegelt. Ich arbeite eng mit Ihnen zusammen, lerne Ihr Geschäft kennen und entwickle Lösungen, die nicht nur kreativ sind, sondern messbare Ergebnisse liefern. Transparenz, Vertrauen und eine partnerschaftliche Zusammenarbeit bilden das Fundament meiner Arbeit.</p>
    </div>
  </section>

  <section class="prices">
    <div class="center">
      <div class="eyebrow">Preise</div>
      <h2 class="section-title">Transparent &amp; fair</h2>
      <p class="lead">Jede Zusammenarbeit wird individuell offeriert und basiert auf einem gemeinsam<br>abgemachten Projektrahmen.</p>
    </div>
    <div class="plans">
      <div class="plan featured">
        <span class="badge">Beliebt</span>
        <h4>Halbtage</h4>
        <div class="price">580 <small>CHF</small></div>
        <ul>
          <li><svg width="9" height="9" viewBox="0 0 10 10" fill="none" stroke="#2fa67d" stroke-width="1.4"><path d="M1.5 5.5l2.2 2.2L8.5 2.5"/></svg>Coaching für ein spezifisches Projekt</li>
          <li><svg width="9" height="9" viewBox="0 0 10 10" fill="none" stroke="#2fa67d" stroke-width="1.4"><path d="M1.5 5.5l2.2 2.2L8.5 2.5"/></svg>Mitarbeit im Unternehmen</li>
          <li><svg width="9" height="9" viewBox="0 0 10 10" fill="none" stroke="#2fa67d" stroke-width="1.4"><path d="M1.5 5.5l2.2 2.2L8.5 2.5"/></svg>Lancierung von Produkten</li>
          <li><svg width="9" height="9" viewBox="0 0 10 10" fill="none" stroke="#2fa67d" stroke-width="1.4"><path d="M1.5 5.5l2.2 2.2L8.5 2.5"/></svg>Relaunch</li>
          <li><svg width="9" height="9" viewBox="0 0 10 10" fill="none" stroke="#2fa67d" stroke-width="1.4"><path d="M1.5 5.5l2.2 2.2L8.5 2.5"/></svg>Marktanalysen</li>
        </ul>
      </div>
      <div class="plan">
        <h4>Einzelstunden</h4>
        <div class="price">180 <small>CHF</small></div>
        <ul>
          <li><svg width="9" height="9" viewBox="0 0 10 10" fill="none" stroke="#2fa67d" stroke-width="1.4"><path d="M1.5 5.5l2.2 2.2L8.5 2.5"/></svg>Erstellen der Marketing Strategie</li>
          <li><svg width="9" height="9" viewBox="0 0 10 10" fill="none" stroke="#2fa67d" stroke-width="1.4"><path d="M1.5 5.5l2.2 2.2L8.5 2.5"/></svg>Sortimentsanalysen mit Massnahmen</li>
          <li><svg width="9" height="9" viewBox="0 0 10 10" fill="none" stroke="#2fa67d" stroke-width="1.4"><path d="M1.5 5.5l2.2 2.2L8.5 2.5"/></svg>Branding</li>
          <li><svg width="9" height="9" viewBox="0 0 10 10" fill="none" stroke="#2fa67d" stroke-width="1.4"><path d="M1.5 5.5l2.2 2.2L8.5 2.5"/></svg>Social Media Inhalte</li>
          <li><svg width="9" height="9" viewBox="0 0 10 10" fill="none" stroke="#2fa67d" stroke-width="1.4"><path d="M1.5 5.5l2.2 2.2L8.5 2.5"/></svg>Website</li>
        </ul>
      </div>
    </div>
    <div class="cta"><span class="btn btn-green">Kostenlose Offerte verlangen</span></div>
  </section>

  <section class="contact">
    <div class="center">
      <div class="eyebrow">Kontakt</div>
      <h2 class="section-title">Lassen Sie uns sprechen</h2>
      <p class="lead">Bereit für professionelles Marketing? Kontaktieren Sie mich für ein unverbindliches<br>Erstgespräch.</p>
    </div>
    <div class="contact-grid">
      <div class="contact-info">
        <h4>Velorusk – Mirela Kovan GmbH</h4>
        <div class="info-row"><svg width="10" height="10" viewBox="0 0 10 10" fill="none" stroke="#2fa67d" stroke-width="1"><path d="M5 9.5S1.5 6 1.5 4a3.5 3.5 0 0 1 7 0c0 2-3.5 5.5-3.5 5.5z"/><circle cx="5" cy="4" r="1.2"/></svg><span>Lindenweg 4<br>CH-6300 Talberg</span></div>
        <div class="info-row"><svg width="10" height="10" viewBox="0 0 10 10" fill="none" stroke="#2fa67d" stroke-width="1"><path d="M2 1h2l1 2.5-1.2.8a5 5 0 0 0 2 2l.8-1.2L9 6v2a1 1 0 0 1-1 1A7 7 0 0 1 1 2a1 1 0 0 1 1-1z"/></svg><span>+41 79 000 12 34</span></div>
        <div class="info-row"><svg width="10" height="10" viewBox="0 0 10 10" fill="none" stroke="#2fa67d" stroke-width="1"><rect x="1" y="2" width="8" height="6" rx="1"/><path d="M1 2.5l4 3 4-3"/></svg><span>info@velorusk.ch</span></div>
        <div class="info-row"><svg width="10" height="10" viewBox="0 0 10 10" fill="#2fa67d"><rect x="1" y="1" width="8" height="8" rx="1"/></svg><span>Kontrabu Profil</span></div>
      </div>
      <div class="form">
        <label>Name</label><div class="field">Ihr Name</div>
        <label>E-Mail</label><div class="field">ihre@email.ch</div>
        <label>Nachricht</label><div class="field area">Wie kann ich Ihnen helfen?</div>
        <div class="submit">Nachricht senden</div>
      </div>
    </div>
  </section>

  <footer class="footer">
    <div class="footer-cols">
      <div class="brand"><span class="brand-square"></span>velorusk</div>
      <div class="footer-col"><h5>Kontakt</h5>Mirela Kovan GmbH<br>Lindenweg 4, CH-6300 Talberg<br>info@velorusk.ch<br>+41 79 000 12 34</div>
      <div class="footer-col"><h5>Rechtliches</h5>Impressum<br>AGB<br>Datenschutz</div>
    </div>
    <div class="footer-bottom">© 2026 Velorusk – Mirela Kovan GmbH. Alle Rechte vorbehalten.</div>
  </footer>

</main>
</body>
</html>
```